Fernlake Business Card Design

We are looking for a fresh business card design for our new logo. We would like a business card that is unique but friendly. We are in the window coverings business offering blinds, shutters and shades for homes.

Target Market(s)

Targeting the end-consumer

Industry/Entity Type

Business

Requirements
Must have
• Must have a dedicates space for a photo of our sales person. Must contain our new logo (attached).

```html
<!DOCTYPE html>
<html lang="en">
<head>
<meta charset="utf-8">
<title>Fernlake Business Card</title>
<link rel="stylesheet" href="https://fonts.googleapis.com/css2?family=Questrial&display=swap">
<style>
  :root {
    --backdrop: #e6e6e6;
    --card: #ffffff;
    --ink: #5b5b5e;
    --ink-dark: #4d4d50;
    --leaf: #7dc242;
    --photo-grey: #c9c9c9;
    --blind-light: #f4f4f4;
    --blind-mid: #d9dadb;
  }
  * { margin: 0; padding: 0; box-sizing: border-box; }
  html, body { width: 1200px; height: 1000px; overflow: hidden; }
  body {
    background: var(--backdrop);
    font-family: "Questrial", "Century Gothic", sans-serif;
    color: var(--ink);
    position: relative;
  }
  .card {
    position: absolute;
    left: 204px;
    width: 790px;
    background: var(--card);
    overflow: hidden;
  }
  .card--front { top: 34px; height: 450px; }
  .card--back { top: 508px; height: 452px; }

  /* Front */
  .staff-photo {
    position: absolute; left: 0; top: 116px;
    width: 218px; height: 218px;
    background: var(--photo-grey);
  }
  .staff-name {
    position: absolute; left: 241px; top: 106px;
    font-size: 60px; line-height: 1; letter-spacing: 0.5px;
    color: var(--ink);
  }
  .staff-role {
    position: absolute; left: 242px; top: 167px;
    font-size: 31px; line-height: 1; letter-spacing: 1px;
    color: var(--leaf);
  }
  .divider {
    position: absolute; left: 241px; top: 211px;
    width: 445px; height: 2px; background: var(--ink);
  }
  .icon-rail {
    position: absolute; left: 241px; top: 211px;
    width: 32px; height: 122px; background: var(--ink);
  }
  .icon-rail svg { position: absolute; left: 6px; width: 20px; height: 20px; }
  .contact-list {
    position: absolute; left: 286px; top: 232px;
    list-style: none;
  }
  .contact-list li {
    font-size: 20px; line-height: 36px; color: var(--ink-dark);
  }
  .brand-mini {
    position: absolute; left: 600px; top: 396px;
    display: flex; align-items: center; gap: 9px;
  }
  .brand-mini .mark { width: 30px; height: 30px; border: 2px solid var(--ink); }
  .brand-mini .wordmark { font-size: 25px; color: var(--ink); }

  /* Back */
  .brand-main {
    position: absolute; left: 48px; top: 177px;
    display: flex; align-items: center; gap: 26px;
  }
  .brand-main .mark { width: 100px; height: 100px; border: 4px solid var(--ink); }
  .brand-main .wordmark { font-size: 76px; line-height: 1; color: var(--ink); }
  .back-url {
    position: absolute; left: 123px; top: 412px;
    font-size: 19px; color: var(--ink-dark);
  }
  .window-photo {
    position: absolute; left: 556px; top: 0;
    width: 234px; height: 452px;
    background: linear-gradient(100deg, var(--blind-mid) 0%, var(--blind-light) 45%, var(--blind-mid) 100%);
  }
  .window-frame {
    position: absolute; left: 576px; top: 22px;
    width: 190px; height: 416px;
    border: 5px solid #ffffff;
  }
</style>
</head>
<body>
  <section class="card card--front">
    <div class="staff-photo" role="img" aria-label="Portrait photo of the sales associate"></div>
    <h1 class="staff-name">DANIEL HART</h1>
    <p class="staff-role">SALES ASSOCIATE</p>
    <div class="divider"></div>
    <div class="icon-rail">
      <svg style="top:25px" viewBox="0 0 20 20" aria-hidden="true">
        <path d="M5 2h3l1 4-2 1.5a10 10 0 0 0 5.5 5.5L14 11l4 1v3a2 2 0 0 1-2 2C9 17 3 11 3 4a2 2 0 0 1 2-2z" fill="#fff"/>
      </svg>
      <svg style="top:61px" viewBox="0 0 20 20" aria-hidden="true" fill="none" stroke="#fff" stroke-width="1.4">
        <circle cx="10" cy="10" r="8"/>
        <ellipse cx="10" cy="10" rx="3.5" ry="8"/>
        <line x1="2" y1="10" x2="18" y2="10"/>
        <line x1="3.5" y1="6" x2="16.5" y2="6"/>
        <line x1="3.5" y1="14" x2="16.5" y2="14"/>
      </svg>
      <svg style="top:97px" viewBox="0 0 20 20" aria-hidden="true" fill="none" stroke="#fff" stroke-width="1.4">
        <rect x="1.5" y="4.5" width="17" height="11"/>
        <polyline points="1.5,4.5 10,11 18.5,4.5"/>
      </svg>
    </div>
    <ul class="contact-list">
      <li>+555.019.2834</li>
      <li>www.fernlakeshutters.com</li>
      <li>daniel.hart@fernlakeshutters.com</li>
    </ul>
    <div class="brand-mini">
      <span class="mark"></span>
      <span class="wordmark">Fernlake</span>
    </div>
  </section>

  <section class="card card--back">
    <div class="brand-main">
      <span class="mark"></span>
      <span class="wordmark">Fernlake</span>
    </div>
    <p class="back-url">www.fernlakeshutters.com</p>
    <div class="window-photo" role="img" aria-label="Close-up photo of white window blinds"></div>
    <div class="window-frame"></div>
  </section>
</body>
</html>
```